Halloween Email Campaign (eMails & Landing Pages)

About Velvets sWhims

Velvet ‘n Whims (VNW) is an e-tailer specializing in fun and flirty outfits and accessories for women, helping them spice up the boring – both in and out of the bedroom. Our focus is on helping our customers play out 3 key characters

1. The Star – Our darling singleton. Always on the hunt for flirty fun mixed with a little bit of naughty and nice – but never alone. She is playful about herself, always adjusting her image. An innocent tease, she captures attention through her provocative appearance and alluring attitude. Perfect for a girl’s night out.

2. The Temptress – Usually in a long term relationship, looking to spice things up with her significant other. Her presence is always highly feminine and sexually charged embodying every male’s fantasy, adding emotional spice through danger and challenge.

3. The Bachelorette –Making the bride’s last night out as a “single lady” a sexy one no one will ever forget! Anything grooving and flashy where they can dress bare and sexy will satisfy. Stretch limo, colourful cocktails or lingerie soiree – whatever they choose, this night is guaranteed to be a riot!
With no geographic boundaries, our audience ranges from somewhat conservative to extremely liberal – forcing us to find ways of adapting all our items to suite the varying tastes.

Our Brand Character
• The Look: Vibrant, Playful, Colourful, Fun and flashy
• The Tone: Humorous, Conversational, Mischievous, Risqué, Adventurous and fun
• The Feel: Exciting, Naughty and Playful

What we’re looking for

We need to design 4 Emails and 4 Landing pages for our Halloween 2010 campaign.

The attached PDF contains the brief for the emails and corresponding landing page (the first landing page is actually our favourite). There are also samples of emails and landing pages to give you an idea of what we're looking for.

Notes:

* We need the designs to be clean and simple. Please be sure to read the above brief on the brand to get a better idea.

* Please visit the website and make sure to feature a costume or two in each our your designs if you plan to show models.

* I'm looking for some creative help - i dont want a rehash of the designs in the brief.

* For a sample of designs from a similar website that is very close to what i'm looking for please check out the "Sample Designs" file

* I dont need all landing pages and emails delivered on the same date. I can take delivery of the first and then within a week take the rest - i need the first to launch...

Any questions? Feel free to bounce them off us…
Oh, just in case – website is currently under construction, you can see it at

http://shop.velvetandwhims.example

Cheers!

Hi All,

Thanks for working on this - for some great examples of what i'm looking for please look at the "Sample Designs" PDF file. These were collected from competing sites but are right up the alley in terms of what we need.

Cheers!

```html
<!DOCTYPE html>
<html lang="en">
<head>
<meta charset="utf-8">
<title>Velvet ‘n Whims — Where’s the Costume Party</title>
<link rel="stylesheet" href="https://fonts.googleapis.com/css2?family=Arimo:wght@400;700&family=Comfortaa:wght@300&family=Great+Vibes&family=Pathway+Gothic+One&display=swap">
<style>
  :root {
    --magenta: #e5007e;
    --magenta-dark: #a8005c;
    --magenta-light: #f05db0;
    --ink: #111111;
    --muted: #8a8a8a;
    --frame: #7d7d7d;
    --paper: #ffffff;
    --feather-1: #e0338f;
    --feather-2: #f6a9cf;
    --model-1: #f3d9e2;
    --model-2: #e9c2cf;
  }
  * { box-sizing: border-box; margin: 0; padding: 0; }
  html, body { width: 1200px; height: 816px; overflow: hidden; background: var(--paper); }
  body { position: relative; font-family: "Arimo", Arial, sans-serif; color: var(--ink); }

  .brand {
    position: absolute; left: 48px; top: 28px;
    font-family: "Arimo", Arial, sans-serif; font-weight: 700; font-size: 30px;
    color: var(--magenta); letter-spacing: -0.5px;
  }

  .account-bar {
    position: absolute; top: 41px; font-size: 11px; color: var(--muted); text-transform: uppercase;
  }
  .account-bar--bag { left: 646px; }
  .account-bar--create { left: 845px; }
  .account-bar--login { left: 958px; }

  .share-button {
    position: absolute; left: 1014px; top: 36px; width: 150px; height: 19px;
    border: 1px solid #b5b5b5; border-radius: 2px; background: linear-gradient(#ffffff, #eeeeee);
    display: flex; align-items: center; gap: 8px; padding-left: 5px;
    font-size: 10px; font-weight: 700; letter-spacing: 1px; color: #333;
  }
  .share-button__square { width: 11px; height: 11px; background: #f36f21; border-radius: 2px; }

  .main-nav {
    position: absolute; left: 31px; top: 77px; width: 1139px; height: 44px;
    border: 1px solid var(--frame); border-bottom: none;
  }
  .main-nav__item {
    position: absolute; top: 10px; font-size: 11px; color: var(--magenta); text-transform: uppercase;
  }
  .search-field {
    position: absolute; left: 855px; top: 7px; width: 168px; height: 24px;
    border: 1px solid #9aa4ae; font-size: 12px; color: #a8a8a8; padding: 4px 3px;
  }
  .search-button {
    position: absolute; left: 1035px; top: 7px; width: 73px; height: 24px;
    border: 1px solid var(--magenta); color: var(--magenta); font-size: 14px;
    display: flex; align-items: center; justify-content: center;
  }

  .hero {
    position: absolute; left: 31px; top: 120px; width: 1139px; height: 660px;
    border: 1px solid var(--frame); overflow: hidden; background: var(--paper);
  }
  .hero__feathers {
    position: absolute; left: 0; top: 264px; width: 665px; height: 396px;
    background: radial-gradient(ellipse 70% 55% at 30% 60%, var(--feather-1) 0%, var(--feather-2) 45%, rgba(255,255,255,0) 75%);
  }
  .hero__model {
    position: absolute; left: 840px; top: 24px; width: 300px; height: 636px;
    background: linear-gradient(180deg, var(--model-1), var(--model-2) 60%, #e7cdb8);
    border-radius: 140px 140px 0 0;
  }
  .hero__kicker {
    position: absolute; left: 209px; top: 112px;
    font-family: "Great Vibes", cursive; font-size: 46px; color: var(--magenta);
  }
  .hero__title {
    position: absolute; left: 56px; top: 146px;
    font-family: "Comfortaa", sans-serif; font-weight: 300; font-size: 92px; color: var(--magenta);
    letter-spacing: -1px; white-space: nowrap;
  }
  .hero__line {
    position: absolute; font-family: "Pathway Gothic One", sans-serif; font-size: 50px; color: var(--ink); white-space: nowrap;
  }
  .hero__line--one { left: 58px; top: 252px; }
  .hero__line--two { left: 389px; top: 300px; }
  .hero__emphasis {
    font-family: "Arimo", Arial, sans-serif; font-weight: 700; font-size: 52px; color: var(--magenta); margin-left: 10px;
  }
  .hero__cta {
    position: absolute; left: 591px; top: 364px; width: 211px; height: 46px;
    background: linear-gradient(180deg, var(--magenta-light) 0%, var(--magenta) 50%, var(--magenta-dark) 100%);
    border: 1px solid var(--magenta-dark);
    display: flex; align-items: center; justify-content: center;
    font-family: "Arimo", Arial, sans-serif; font-weight: 700; font-size: 30px; color: #fff; letter-spacing: -0.5px;
  }

  .footer-links {
    position: absolute; top: 788px; font-size: 11px; text-transform: uppercase; white-space: nowrap;
  }
  .footer-links--service { left: 34px; color: var(--magenta); }
  .footer-links--legal { right: 38px; color: var(--muted); }
  .footer-links__sep { margin: 0 6px; }
</style>
</head>
<body>
  <div class="brand">Velvet ‘n Whims</div>

  <div class="account-bar account-bar--bag">Your shopping bag is empty</div>
  <div class="account-bar account-bar--create">Create account</div>
  <div class="account-bar account-bar--login">Login</div>
  <div class="share-button"><span class="share-button__square"></span>SHARE</div>

  <nav class="main-nav">
    <span class="main-nav__item" style="left:16px">Whats new</span>
    <span class="main-nav__item" style="left:133px">Blog</span>
    <span class="main-nav__item" style="left:217px">Accessories</span>
    <span class="main-nav__item" style="left:337px">Baby dolls</span>
    <span class="main-nav__item" style="left:443px">Club-wear</span>
    <span class="main-nav__item" style="left:549px">Costumes</span>
    <span class="main-nav__item" style="left:641px">Dresses</span>
    <span class="main-nav__item" style="left:723px">Sales &amp; Specials</span>
    <div class="search-field">enter keyword</div>
    <div class="search-button">Search</div>
  </nav>

  <section class="hero">
    <div class="hero__feathers" role="img" aria-label="Soft swirl of pink and magenta feathers"></div>
    <div class="hero__model" role="img" aria-label="Model in a pale pink fairy costume with sheer wings"></div>
    <div class="hero__kicker">Where’s the</div>
    <h1 class="hero__title">Costume Party</h1>
    <p class="hero__line hero__line--one">Be whatever you want to be.</p>
    <p class="hero__line hero__line--two">Live out your<span class="hero__emphasis">FANTASY</span></p>
    <div class="hero__cta">Shop Now</div>
  </section>

  <footer>
    <div class="footer-links footer-links--service">Secure online shopping<span class="footer-links__sep">|</span>Check order status<span class="footer-links__sep">|</span>Customer service<span class="footer-links__sep">|</span>Contact us<span class="footer-links__sep">|</span>Your account</div>
    <div class="footer-links footer-links--legal">Privacy &amp; security<span class="footer-links__sep">|</span>Conditions of use<span class="footer-links__sep">|</span>Satisfaction guranteed</div>
  </footer>
</body>
</html>
```